Business Card Design - Law Firm

We are a boutique law firm located near the beach in Manly, Australia. We have recently had a new logo designed and are revamping our business cards with the new logo.

We have recently had a business card design done for us but are not entirely happy with it. We are looking for something modern, simplistic but striking. We would like to see multiple designs.

We have attached a word document which includes our new logo and the current business card design which we are looking at moving away from.

We would like the business cards to be double sided. We would like the design to include something which we can print in gloss colour when we send it to the business card printers.

```html
<!DOCTYPE html>
<html lang="en">
<head>
<meta charset="utf-8">
<title>Harbourne &amp; Partners – Business Card</title>
<link rel="stylesheet" href="https://fonts.googleapis.com/css2?family=Poppins:wght@400;500;600;700&display=swap">
<style>
  :root {
    --backdrop: #d6d7da;
    --navy: #2b2f97;
    --navy-soft: #4049b0;
    --gold: #b79a4e;
    --silver: #c9cbd0;
    --ink: #2a2a2e;
    --grey-text: #6d6e73;
    --paper: #ffffff;
  }
  * { box-sizing: border-box; margin: 0; padding: 0; }
  html, body {
    width: 1171px; height: 1200px; overflow: hidden;
    background: var(--backdrop);
    font-family: "Poppins", sans-serif;
  }
  .sheet {
    width: 1171px; height: 1200px;
    display: flex; flex-direction: column; align-items: center; justify-content: center;
    gap: 60px;
  }
  .card {
    position: relative;
    width: 900px; height: 514px;
    overflow: hidden;
    box-shadow: 0 10px 30px rgba(0,0,0,0.18);
  }

  /* Back side */
  .card-back {
    background: var(--navy);
    display: flex; align-items: center; justify-content: center; gap: 22px;
  }
  .card-back .brand-dot {
    width: 56px; height: 56px; border-radius: 50%;
    background: var(--navy-soft);
  }
  .card-back .brand-name {
    font-weight: 600; font-size: 40px; letter-spacing: 0.5px;
    color: var(--navy-soft);
  }

  /* Front side */
  .card-front { background: var(--paper); }
  .brand {
    position: absolute; left: 60px; top: 210px;
    display: flex; align-items: center; gap: 16px;
  }
  .brand-dot {
    width: 42px; height: 42px; border-radius: 50%;
    background: var(--navy);
  }
  .brand .brand-name {
    font-weight: 600; font-size: 27px; color: var(--ink);
  }
  .divider {
    position: absolute; left: 478px; top: 80px;
    width: 2px; height: 210px; background: var(--gold);
  }
  .details {
    position: absolute; left: 508px; top: 72px;
    color: var(--grey-text); font-size: 15px; line-height: 1.7;
  }
  .person-name {
    font-weight: 700; font-size: 27px; color: var(--navy);
    line-height: 1.2; letter-spacing: -0.3px;
  }
  .person-role { font-size: 16px; margin-bottom: 12px; }
  .address { margin-bottom: 14px; }
  .contact-list { list-style: none; }
  .contact-list li { display: flex; align-items: center; gap: 10px; }
  .contact-list svg { width: 14px; height: 14px; flex: none; fill: var(--navy); }
  .wave { position: absolute; left: 0; top: 0; width: 900px; height: 514px; }
</style>
</head>
<body>
<main class="sheet">

  <section class="card card-back" aria-label="Card back">
    <span class="brand-dot"></span>
    <span class="brand-name">Harbourne &amp; Partners</span>
  </section>

  <section class="card card-front" aria-label="Card front">
    <svg class="wave" viewBox="0 0 900 514" aria-hidden="true">
      <path d="M0,490 C300,486 620,430 900,352 L900,514 L0,514 Z" fill="var(--navy)"/>
      <path d="M0,474 C300,470 620,412 900,334" fill="none" stroke="var(--gold)" stroke-width="7"/>
      <path d="M0,460 C300,456 620,398 900,320" fill="none" stroke="var(--silver)" stroke-width="3"/>
    </svg>

    <div class="brand">
      <span class="brand-dot"></span>
      <span class="brand-name">Harbourne &amp; Partners</span>
    </div>

    <div class="divider"></div>

    <div class="details">
      <h1 class="person-name">MAYA LINTON</h1>
      <p class="person-role">Practice Manager</p>
      <p class="address">Suite 4, 12 Coral Street<br>BRINEWOOD NSW 2190</p>
      <ul class="contact-list">
        <li>
          <svg viewBox="0 0 24 24"><path d="M6.6 10.8a15.1 15.1 0 0 0 6.6 6.6l2.2-2.2a1 1 0 0 1 1-.25 11.4 11.4 0 0 0 3.6.57 1 1 0 0 1 1 1V20a1 1 0 0 1-1 1A17 17 0 0 1 3 4a1 1 0 0 1 1-1h3.5a1 1 0 0 1 1 1c0 1.25.2 2.45.57 3.57a1 1 0 0 1-.25 1z"/></svg>
          (02) 9000 4187
        </li>
        <li>
          <svg viewBox="0 0 24 24"><path d="M2 5h20v14H2z M4 7v.4l8 5 8-5V7z" fill-rule="evenodd"/></svg>
          maya.linton@harbournelaw.com.au
        </li>
        <li>
          <svg viewBox="0 0 24 24"><circle cx="12" cy="12" r="10"/></svg>
          www.harbourneandpartners.com.au
        </li>
      </ul>
    </div>
  </section>

</main>
</body>
</html>
```